Real Estate Marketing Postcards need a fresh look, Front & Back

I have a current postcard design (attached) that lacks design quality and too much use of color. I do like the basic color scheme, but I'm open to anything that cleans up the look and incorporates space for the existing text. I'm not opposed to a design with a white background, more white space. The design should be full bleed according to the attached specs. I would like this to be sent over in an Adobe format, something like InDesign.

The company logo will remain the same colors and appearance. The headshot will likely be updated in the coming weeks.

I am attaching a sample of a recent card plus a template from the printer showing the back of the card and location of the address and postage section that must remain blank. I am also including the logo and another logo designed for use with a white (or non blue) background.

(feel free to swap in stock photos of whatever house you want, but the front of the card should incorporate at least one photo of a house.)

Target Market(s)

Home owners.

Industry/Entity Type

Real Estate

Font styles to use
Sans Serif

Colors

Designer to choose colors to be used in the design.

Requirements
Must have
• Company logo, the headshot, the contact info on the back, a photo or photos of a house along with the text "Just Sold" or "Sold" featured on the front of the card.

```html
<!DOCTYPE html>
<html lang="en">
<head>
<meta charset="utf-8">
<title>Just Sold Postcard – Front &amp; Back</title>
<link href="https://fonts.googleapis.com/css2?family=Montserrat:wght@500;600;700;800&family=Open+Sans:ital,wght@0,400;0,600;1,700&display=swap" rel="stylesheet">
<style>
  :root {
    --navy: #0f2f55;
    --navy-deep: #0a2545;
    --navy-light: #1b4a7c;
    --lime: #a8c93a;
    --sky-line: #8fc7ea;
    --paper: #ffffff;
    --mail-grey: #e6e6e6;
    --ink: #0f2f55;
    --stage: #eeeeee;
  }
  * { box-sizing: border-box; margin: 0; padding: 0; }
  html, body { width: 1200px; height: 511px; overflow: hidden; }
  body {
    background: var(--stage);
    position: relative;
    font-family: "Open Sans", Arial, sans-serif;
  }
  .postcard {
    position: absolute;
    top: 71px;
    width: 521px;
    height: 370px;
    overflow: hidden;
    background: var(--paper);
  }
  .postcard--front { left: 58px; }
  .postcard--back { left: 622px; }

  /* ---------- Front ---------- */
  .front-photo {
    position: absolute; left: 0; top: 0; width: 320px; height: 350px;
    background: linear-gradient(180deg, #6d6fa6 0%, #a393b8 35%, #5d6b82 62%, #3d4552 100%);
  }
  .front-panel { position: absolute; inset: 0; width: 521px; height: 350px; }
  .front-headline {
    position: absolute; right: 6px; top: 146px; width: 250px; text-align: left;
    font-family: "Montserrat", Arial, sans-serif;
  }
  .front-headline__title {
    color: #fff; font-weight: 700; font-size: 35px; line-height: 1; letter-spacing: 0.2px;
  }
  .front-headline__brand {
    color: var(--lime); font-weight: 700; font-size: 14.5px; letter-spacing: 1.4px; margin-top: 6px;
  }
  .front-headline__tagline {
    color: #fff; font-weight: 500; font-size: 10.5px; letter-spacing: 1.3px; margin-top: 3px;
  }
  .front-footer {
    position: absolute; left: 0; bottom: 0; width: 100%; height: 20px;
    background: var(--lime); color: var(--navy-deep);
    font-family: "Montserrat", Arial, sans-serif; font-weight: 600; font-size: 9.5px;
    display: flex; align-items: center; justify-content: center; padding-left: 90px;
  }

  /* ---------- Back ---------- */
  .back-header { position: absolute; left: 0; top: 0; width: 521px; height: 70px; }
  .back-header__title {
    position: absolute; top: 13px; width: 100%; text-align: center;
    font-family: "Montserrat", Arial, sans-serif; font-weight: 600;
    font-size: 27px; letter-spacing: 4px; color: var(--lime);
  }
  .back-pitch {
    position: absolute; top: 106px; width: 100%; text-align: center;
    font-style: italic; font-weight: 700; font-size: 11.5px; line-height: 17px;
    color: var(--ink); letter-spacing: 0.3px;
  }
  .agent-photo {
    position: absolute; left: 22px; top: 151px; width: 104px; height: 108px;
    border: 6px solid var(--navy); background: #fff; padding: 3px;
  }
  .agent-photo__fill {
    width: 100%; height: 100%;
    background: linear-gradient(180deg, #8e8a86 0%, #b7b1aa 55%, #dfe3ea 100%);
  }
  .brand-lockup {
    position: absolute; left: 170px; top: 193px;
    display: flex; align-items: center; gap: 7px;
    font-family: "Montserrat", Arial, sans-serif; font-weight: 700; font-size: 19px;
    color: var(--navy);
  }
  .brand-lockup__dot { width: 12px; height: 12px; border-radius: 50%; background: var(--lime); }
  .agent-contact {
    position: absolute; left: 362px; top: 162px;
    font-size: 10.5px; line-height: 12.8px; color: var(--ink); letter-spacing: 0.2px;
  }
  .divider { position: absolute; left: 0; top: 253px; width: 521px; height: 14px; }
  .mail-area {
    position: absolute; left: 0; top: 263px; width: 100%; height: 107px;
    background: var(--mail-grey);
  }
</style>
</head>
<body>

  <!-- Front of card -->
  <section class="postcard postcard--front">
    <div class="front-photo" role="img" aria-label="Photo of a two-storey house at dusk with lit garage and wet driveway"></div>
    <svg class="front-panel" viewBox="0 0 521 350" aria-hidden="true">
      <defs>
        <radialGradient id="panelGlow" cx="0.62" cy="0.5" r="0.7">
          <stop offset="0" stop-color="#1d4b7d"/>
          <stop offset="1" stop-color="#0b2748"/>
        </radialGradient>
      </defs>
      <path d="M292 0 Q228 170 282 350 L521 350 L521 0 Z" fill="var(--sky-line)"/>
      <path d="M300 0 Q236 170 290 350 L521 350 L521 0 Z" fill="url(#panelGlow)"/>
    </svg>
    <div class="front-headline">
      <div class="front-headline__title">JUST SOLD!</div>
      <div class="front-headline__brand">THE OAKMONT REALTOR</div>
      <div class="front-headline__tagline">You Know It Won't Last Long!</div>
    </div>
    <div class="front-footer">www.oakmonthomes.com</div>
  </section>

  <!-- Back of card -->
  <section class="postcard postcard--back">
    <svg class="back-header" viewBox="0 0 521 70" aria-hidden="true">
      <path d="M0 0 H521 V60 H155 Q140 60 130 52 Q122 46 108 46 H0 Z" fill="var(--navy)"/>
      <path d="M0 50 H108 Q122 50 130 56 Q140 64 155 64 H521" fill="none" stroke="var(--lime)" stroke-width="5"/>
    </svg>
    <div class="back-header__title">SELLING?</div>

    <p class="back-pitch">There is no other agent who knows the Oakmont market better.<br>Contact me today to get your home SOLD.</p>

    <div class="agent-photo">
      <div class="agent-photo__fill" role="img" aria-label="Agent headshot"></div>
    </div>

    <div class="brand-lockup">
      <span class="brand-lockup__dot"></span>
      <span class="brand-lockup__name">Birchfield Realty</span>
    </div>

    <address class="agent-contact" style="font-style:normal">
      Dario Vellani<br>
      "The Oakmont Realtor<br>
      Birchfield Realty<br>
      (555) 214-0300 Office<br>
      (555) 386-7142 Cell<br>
      www.oakmonthomes.com
    </address>

    <div class="mail-area"></div>
    <svg class="divider" viewBox="0 0 521 14" aria-hidden="true">
      <line x1="22" y1="2" x2="500" y2="2" stroke="var(--navy)" stroke-width="3"/>
      <path d="M256 2 L270 2 L263 10 Z" fill="var(--navy)"/>
    </svg>
  </section>

</body>
</html>
```